Blue Heron Business Card

This is a business card for a printing company but I actually don't have a logo. Just need to typeset the words "Blue Heron Printing" as the logo. Then add my name "Marla Vossen" + phone number + address

Target Market(s)

ceos and professionals

Industry/Entity Type

printing and manufacturing

Contact Information for Business Card

Blue Heron Printing/ 4817 dunmore ave. S. Fern Hollow, CA 90418/ 318-447-3092/ Marla Vossen

Font styles to use
Serif
Other font styles liked:
• a modern font would be nice

Colors
0054AA
0677BA
7BADD7
CADEEF
E8F1F8
0094D4
00A9DD
6FCCEA
C7EBF8
E9F6FB

Requirements
Must have
• company name, number, address
Nice to have
• nice bold feel
Should not have
• nothing in particular

```html
<!DOCTYPE html>
<html lang="en">
<head>
<meta charset="utf-8">
<title>Blue Heron Business Card</title>
<link href="https://fonts.googleapis.com/css2?family=Bebas+Neue&family=Montserrat:wght@400;700&display=swap" rel="stylesheet">
<style>
  :root {
    --backdrop: #d9d9d6;
    --card: #333333;
    --edge: #00a9dd;
    --accent: #0094d4;
    --ink-light: #e9e9e9;
    --wordmark: #9a9a9a;
  }
  * { margin: 0; padding: 0; box-sizing: border-box; }
  html, body {
    width: 1200px;
    height: 801px;
    overflow: hidden;
    background: var(--backdrop);
  }
  .canvas {
    width: 1200px;
    height: 801px;
    display: flex;
    align-items: center;
    justify-content: center;
    gap: 40px;
  }
  .card {
    width: 520px;
    height: 297px;
    background: var(--card);
    border-bottom: 3px solid var(--edge);
    border-left: 2px solid var(--edge);
    box-shadow: 0 10px 24px rgba(0, 0, 0, 0.18);
  }
  .card-front {
    display: flex;
    align-items: center;
  }
  .holder-name {
    width: 262px;
    padding-right: 22px;
    text-align: right;
    font-family: "Montserrat", sans-serif;
    font-weight: 700;
    font-size: 19px;
    letter-spacing: 0.5px;
    color: var(--accent);
    text-transform: uppercase;
    white-space: nowrap;
  }
  .divider {
    width: 1px;
    height: 64px;
    background: var(--accent);
  }
  .contact {
    padding-left: 20px;
    font-family: "Montserrat", sans-serif;
    font-style: normal;
    font-weight: 400;
    font-size: 12.5px;
    line-height: 1.45;
    color: var(--ink-light);
    white-space: nowrap;
  }
  .contact-phone {
    display: flex;
    align-items: center;
    gap: 5px;
  }
  .phone-icon { width: 11px; height: 11px; }
  .card-back {
    display: flex;
    align-items: center;
    justify-content: center;
  }
  .wordmark {
    font-family: "Bebas Neue", sans-serif;
    font-size: 58px;
    letter-spacing: 1px;
    color: var(--wordmark);
    white-space: nowrap;
  }
</style>
</head>
<body>
  <main class="canvas">
    <section class="card card-front" aria-label="Business card front">
      <h1 class="holder-name">Marla Vossen</h1>
      <span class="divider"></span>
      <address class="contact">
        <div>4817 dunmore ave.</div>
        <div>S. Fern Hollow, CA 90418</div>
        <div class="contact-phone">
          <svg class="phone-icon" viewBox="0 0 24 24" aria-hidden="true">
            <path fill="var(--accent)" d="M6.6 10.8a15.1 15.1 0 0 0 6.6 6.6l2.2-2.2a1 1 0 0 1 1-.25 11.4 11.4 0 0 0 3.6.57 1 1 0 0 1 1 1V20a1 1 0 0 1-1 1A17 17 0 0 1 3 4a1 1 0 0 1 1-1h3.5a1 1 0 0 1 1 1c0 1.25.2 2.45.57 3.57a1 1 0 0 1-.25 1z"/>
          </svg>
          <span>318-447-3092</span>
        </div>
      </address>
    </section>
    <section class="card card-back" aria-label="Business card back">
      <div class="wordmark">Blue Heron Printing</div>
    </section>
  </main>
</body>
</html>
```